Sonstige Web-Design für Private Cloud Lösungen
Zielgruppe
Wir sind anbieter für Private Cloud Lösungen und benötigen eine Zeitgemäße Website, die ohne viel schnick schnack klar ausdrückt was wir machen.
Dabei die nötige Seriösität ausdrückt, welche hochsensible Daten benötigen.
Unsere Zielgruppe sind Unternehmen bis 250 MA
Die Farbgebung sollte an die des Logos angepasst sein, welches hier ebenfalls mit Farbcode hochgeladen wird.
Der Focus liegt auf Managed private Cloud und dem klaren kommitment Ihre Daten sicher in Deutschland
von der Landingpage soll es zur maximal 5 Unterseiten gehen.
1. Managed Private Cloud
2. Service Provider (Hier sollen unsere Dienstleistungen gelistet und auf einzelnen Seiten erklärt werden)
3. Trainings
4. Kontakt
Aufgabenstellung
Es sollte modern sein. Beim Besuch der Website soll auf der ersten Seite klar werden, was den Besucher erwartet jedoch ohne viel Worte.

```html
<!DOCTYPE html>
<html lang="de">
<head>
<meta charset="utf-8">
<title>Nordvia – Private-Cloud-Lösungen</title>
<link href="https://fonts.googleapis.com/css2?family=Roboto:wght@400;500;700&display=swap" rel="stylesheet">
<style>
:root{
  --blue:#0b95c9;
  --black:#000;
  --dark:#2f2f2f;
  --card:#232323;
  --white:#fff;
  --ink:#1e1e1e;
  --grey:#6b6b6b;
}
*{margin:0;padding:0;box-sizing:border-box}
html,body{width:1200px;height:3234px;overflow:hidden}
body{font-family:'Roboto',sans-serif;background:var(--dark);color:var(--white);position:relative}
.abs{position:absolute}

/* Hero */
.hero{left:0;top:0;width:1200px;height:674px;background:var(--black)}
.hero-photo{left:0;top:90px;width:1200px;height:584px;
  background:radial-gradient(ellipse 420px 360px at 380px 300px,#3a2d25 0%,#1c1713 45%,transparent 80%),
             radial-gradient(ellipse 500px 400px at 880px 260px,#2a2f36 0%,#15181c 50%,transparent 85%),#060606}
.brand{left:95px;top:34px;height:64px;display:flex;align-items:center;gap:10px}
.brand-name{font-size:30px;font-weight:500;color:var(--white);letter-spacing:1px}
.brand-square{width:14px;height:14px;background:var(--blue)}
.nav{top:62px;font-size:17px;font-weight:500;color:var(--white)}
.nav.active{color:var(--blue)}
.hero-title{left:538px;top:326px;font-size:45px;font-weight:700;line-height:56px}
.hero-text{left:538px;top:382px;width:520px;font-size:16px;font-weight:500;line-height:26px}

/* Partners */
.partners{left:0;top:674px;width:1200px;height:167px;background:var(--white)}
.partner{top:742px;height:40px;display:flex;align-items:center;gap:10px;font-size:24px;font-weight:500}
.partner .dot{width:22px;height:22px;border-radius:50%}

/* Intro */
.intro-title{left:0;width:1200px;top:934px;text-align:center;font-size:35px;font-weight:700}
.intro-text{left:250px;width:700px;top:988px;text-align:center;font-size:16px;font-weight:500;line-height:26px}

.card{top:1084px;width:293px;height:318px;background:var(--card);box-shadow:0 0 18px rgba(255,255,255,.22);text-align:center}
.card svg{margin-top:20px}
.card h3{margin-top:22px;font-size:27px;font-weight:700;color:var(--blue)}
.card p{margin:14px auto 0;width:265px;font-size:16px;font-weight:500;line-height:26px}

/* Feature rows */
.label{font-size:16px;font-weight:500}
.feature-title{font-size:31px;font-weight:700;line-height:38px}
.feature-text{width:400px;font-size:16px;font-weight:500;line-height:26px}
.btn{display:flex;align-items:center;justify-content:center;background:var(--blue);color:var(--white);border-radius:5px;font-weight:700}
.btn-small{width:185px;height:40px;font-size:16px}
.photo{border-radius:1px}

/* CTA */
.cta{left:0;top:2918px;width:1200px;height:316px;background:var(--white)}
.cta-title{left:0;width:1200px;top:2984px;text-align:center;font-size:45px;font-weight:700;color:var(--blue)}
.cta-text{left:250px;width:700px;top:3046px;text-align:center;font-size:16px;font-weight:500;line-height:26px;color:var(--ink)}
.btn-large{left:395px;top:3122px;width:410px;height:59px;font-size:22px}
</style>
</head>
<body>

<section class="abs hero"></section>
<div class="abs hero-photo" role="img" aria-label="Dunkles Foto: Techniker steckt Netzwerkkabel an einem Serverschrank"></div>

<div class="abs brand"><span class="brand-name">Nordvia</span><span class="brand-square"></span></div>
<nav>
  <a class="abs nav active" style="left:463px">Start</a>
  <a class="abs nav" style="left:545px">Managed Privat Cloud</a>
  <a class="abs nav" style="left:759px">Service Provider</a>
  <a class="abs nav" style="left:931px">Trainings</a>
  <a class="abs nav" style="left:1045px">Kontakt</a>
</nav>

<h1 class="abs hero-title">Private-Cloud-Lösungen</h1>
<p class="abs hero-text">Lorem ipsum dolor sit amet, consectetuer adipiscing elit Aenean com modo ligula eget dolor. Aenean massa. Cum sociis natoque penatibus et magen piscing elit ligula eget dolor.</p>

<section class="abs partners"></section>
<div class="abs partner" style="left:135px;color:#222"><span class="dot" style="background:#e2231a"></span>Wachtfels</div>
<div class="abs partner" style="left:368px;color:var(--blue)"><span class="dot" style="background:var(--blue)"></span>Wolkenhaus</div>
<div class="abs partner" style="left:570px;color:#a23a3f"><span class="dot" style="background:#a23a3f"></span>Teamwerk</div>
<div class="abs partner" style="left:880px;color:#222"><span class="dot" style="background:#f07c1a"></span>Postarchiv</div>

<h2 class="abs intro-title">Schöpfen Sie Ihr volles Potenzial aus.</h2>
<p class="abs intro-text">Lorem ipsum dolor sit amet, consectetuer adipiscing elit Aenean com modo ligula eget dolor. Aenean massa. Cum sociis natoque penatibus escing elit ligula eget dolor.</p>

<div class="abs card" style="left:112px">
  <svg width="80" height="80" viewBox="0 0 80 80" fill="var(--blue)">
    <rect x="6" y="12" width="8" height="64"/><rect x="18" y="36" width="8" height="40"/>
    <rect x="30" y="48" width="8" height="28"/><rect x="42" y="56" width="8" height="20"/>
    <rect x="54" y="62" width="8" height="14"/><rect x="4" y="72" width="70" height="5"/>
    <circle cx="46" cy="28" r="13" fill="none" stroke="var(--blue)" stroke-width="4"/>
    <path d="M58 38 L70 52 L66 54 L74 58 L72 48 L68 50 L60 36Z"/>
  </svg>
  <h3>Kosten senken</h3>
  <p>Aenean com modo ligula eget dolor. Aenean massa. Cum sociis natoque pena tibus escing elit ligula eget dolor.</p>
</div>

<div class="abs card" style="left:453px">
  <svg width="80" height="80" viewBox="0 0 80 80" fill="var(--blue)">
    <rect x="27" y="6" width="3" height="40"/><rect x="39" y="6" width="3" height="40"/>
    <rect x="51" y="6" width="3" height="40"/><rect x="63" y="6" width="3" height="40"/>
    <circle cx="28.5" cy="18" r="5"/><circle cx="40.5" cy="30" r="5"/>
    <circle cx="52.5" cy="14" r="5"/><circle cx="64.5" cy="34" r="5"/>
    <rect x="4" y="50" width="12" height="24" rx="2"/>
    <path d="M18 52 Q34 46 46 54 L58 54 Q64 54 62 60 L44 60 L46 62 Q66 62 74 52 Q78 56 72 62 Q58 76 40 74 L18 72Z"/>
  </svg>
  <h3>Mehr Kontrolle</h3>
  <p>Lorem ipsum dolor sit amet, conse ctetuer adipiscing elit Aenean com modo ligula eget dolor. Aenean massa.</p>
</div>

<div class="abs card" style="left:794px">
  <svg width="96" height="90" viewBox="0 0 96 90" fill="none" stroke="var(--blue)" stroke-width="4">
    <ellipse cx="48" cy="8" rx="10" ry="5"/><path d="M38 8v14c0 6 20 6 20 0V8"/>
    <ellipse cx="14" cy="32" rx="9" ry="4"/><path d="M5 32v12c0 5 18 5 18 0V32"/>
    <ellipse cx="82" cy="32" rx="9" ry="4"/><path d="M73 32v12c0 5 18 5 18 0V32"/>
    <ellipse cx="48" cy="70" rx="10" ry="5"/><path d="M38 70v12c0 6 20 6 20 0V70"/>
    <path d="M48 28v34M48 44l-18-6M48 44l18-6M42 56l6 6 6-6"/>
  </svg>
  <h3>Leichter Skalieren</h3>
  <p>Lorem ipsum dolor sit amet, conse ctetuer adipiscing elit Aenean com modo ligula eget dolor. Aenean massa.</p>
</div>

<!-- Feature: Managed Privat Cloud -->
<p class="abs label" style="left:138px;top:1569px">Managed Privat Cloud</p>
<h2 class="abs feature-title" style="left:138px;top:1598px">Ihre Daten in Deutschland</h2>
<p class="abs feature-text" style="left:138px;top:1651px">Lorem ipsum dolor sit amet, consectetuer adipiscing elit Aenean com modo ligula eget dolor. Aenean massa. Cum sociis natoque penatibus escing elit ligula eget dolor.</p>
<a class="abs btn btn-small" style="left:138px;top:1772px">Zum Überblick</a>
<div class="abs photo" style="left:599px;top:1568px;width:417px;height:271px;background:linear-gradient(180deg,#8fb3d9 0%,#c9d6e4 45%,#8c8a86 75%,#5f5d59 100%)" role="img" aria-label="Foto: Deutschlandflagge vor einem historischen Parlamentsgebäude"></div>

<!-- Feature: Service Provider -->
<div class="abs photo" style="left:95px;top:2007px;width:417px;height:270px;background:linear-gradient(180deg,#cfd6e0 0%,#3a4252 35%,#2b2f38 55%,#dfe3ea 75%,#eef1f5 100%)" role="img" aria-label="Foto: Rechenzentrum mit Serverreihen und hellem Boden"></div>
<p class="abs label" style="left:599px;top:2009px">Service Provider</p>
<h2 class="abs feature-title" style="left:599px;top:2039px">Der Full Service Provider<br>für den Mittelstand</h2>
<p class="abs feature-text" style="left:599px;top:2124px">Lorem ipsum dolor sit amet, consectetuer adipiscing elit Aenean com modo ligula eget dolor. Aenean massa. Cum sociis natoque penatibus escing elit ligula eget dolor.</p>
<a class="abs btn btn-small" style="left:600px;top:2245px">Zum Überblick</a>

<!-- Feature: Trainings -->
<p class="abs label" style="left:138px;top:2475px">Trainings</p>
<h2 class="abs feature-title" style="left:138px;top:2507px">IT-Training für Unter-<br>nehmen - Wir bringen Sie<br>weiter</h2>
<p class="abs feature-text" style="left:138px;top:2635px">Lorem ipsum dolor sit amet, consectetuer adipiscing elit Aenean com modo ligula eget dolor. Aenean massa. Cum sociis natoque penatibus escing elit ligula eget dolor.</p>
<a class="abs btn btn-small" style="left:138px;top:2755px">Zum Überblick</a>
<div class="abs photo" style="left:599px;top:2484px;width:419px;height:271px;background:linear-gradient(135deg,#5a4a3e 0%,#9a8a78 40%,#3a3028 70%,#1e1a16 100%)" role="img" aria-label="Foto: Schulungsraum mit Teilnehmenden an Laptops und einem Trainer"></div>

<!-- CTA -->
<section class="abs cta"></section>
<h2 class="abs cta-title">Sie möchten mehr erfahren?</h2>
<p class="abs cta-text">Lorem ipsum dolor sit amet, consectetuer adipiscing elit Aenean com modo ligula eget dolor. Aenean massa. Cum sociis natoque penatibus escing elit ligula eget dolor.</p>
<a class="abs btn btn-large">Mit einem Experten sprechen</a>

</body>
</html>
```